KIRO Nature Soap

We need to design new product Nature and medicative Soap.Made in Malaysia
* 100% natural.
* made from nature JUNGLE OIL.
* Very effective for Acne & Skin irritation
* size 100 Gm.
* Use for all skin types including sensitive skin
* Name of the product " KIRO Soap"

Reason: please I need to extended since I haven't receive any suitable design for my project

Target Market(s)

International

Industry/Entity Type

Hair And Beauty

Font styles to use
Serif

Colors
33a6d7
abd037
fbed22

Requirements
Must have
• * must have English- Arabic ingredient
• * Very effective for Acne & Skin irritation
Nice to have
• * some things related to natural (water,tree,face..)
• * Show faces picture (after - before)

```html
<!DOCTYPE html>
<html lang="en">
<head>
<meta charset="utf-8">
<title>KIRO Soap – Jungle Oil Labels</title>
<link href="https://fonts.googleapis.com/css2?family=Alegreya+SC:wght@500;700&family=Alegreya:ital,wght@0,400;0,500;1,400&display=swap" rel="stylesheet">
<style>
  :root {
    --bg-center: #cfe9ec;
    --bg-edge: #a3cdd2;
    --leaf-light: #a9cf7e;
    --leaf-mid: #6fa55a;
    --leaf-dark: #3f7a4a;
    --paper: #ece8df;
    --brand-blue: #4a7db6;
    --brown: #6a3b1f;
    --ink: #2f2a26;
    --frame: #6a3b1f;
    --accent-green: #9cc63a;
    --face-tone: #e4c9a8;
  }
  * { margin: 0; padding: 0; box-sizing: border-box; }
  html, body { width: 1197px; height: 1200px; overflow: hidden; }
  body {
    position: relative;
    background: radial-gradient(ellipse at 50% 45%, var(--bg-center) 0%, var(--bg-edge) 100%);
    font-family: "Alegreya", Georgia, serif;
    color: var(--ink);
  }
  .label {
    position: absolute;
    left: 270px;
    width: 690px;
    height: 414px;
    border-radius: 34px;
    overflow: hidden;
    box-shadow: 14px 14px 22px rgba(40, 50, 55, 0.55);
  }
  .label--front { top: 129px; }
  .label--back { top: 610px; }
  .leaf-field {
    position: absolute; inset: 0;
    background:
      radial-gradient(circle at 15% 30%, var(--leaf-dark) 0%, transparent 35%),
      radial-gradient(circle at 85% 70%, var(--leaf-dark) 0%, transparent 30%),
      radial-gradient(circle at 90% 20%, var(--leaf-light) 0%, transparent 40%),
      radial-gradient(circle at 10% 85%, var(--leaf-light) 0%, transparent 40%),
      linear-gradient(135deg, var(--leaf-mid), var(--leaf-light) 50%, var(--leaf-mid));
  }
  .panel {
    position: absolute;
    top: 0; bottom: 0;
    left: 159px;
    width: 373px;
    background: var(--paper);
  }
  .panel-frame {
    position: absolute;
    top: -2px; bottom: 32px;
    left: 17px; right: 17px;
    border: 1.5px solid var(--frame);
    border-top: none;
  }
  .label--front .panel-frame { border-color: var(--ink); }
  .label--back .panel-frame { top: 0; bottom: 20px; border-top: 1.5px solid var(--frame); }
  .content { position: absolute; inset: 0; text-align: center; }
  .brand-mark {
    position: absolute;
    left: 50%;
    transform: translateX(-50%);
    border-radius: 50%;
    background: var(--brand-blue);
  }
  .brand-name {
    position: absolute; left: 0; right: 0;
    font-family: "Alegreya SC", Georgia, serif;
    font-weight: 700;
    color: var(--brand-blue);
    letter-spacing: 0.5px;
  }
  .brand-name .dot { display: inline-block; width: 5px; height: 5px; border-radius: 50%; background: var(--brand-blue); vertical-align: middle; margin: 0 10px; }
  .dotted-rule { position: absolute; border-top: 2px dotted var(--brown); }
  .product-name {
    position: absolute; left: 0; right: 0;
    font-family: "Alegreya SC", Georgia, serif;
    font-weight: 500;
    color: var(--brown);
  }
  /* front */
  .label--front .brand-mark { top: 40px; width: 62px; height: 62px; }
  .label--front .brand-name { top: 136px; font-size: 42px; }
  .label--front .dotted-rule { top: 194px; left: 39px; right: 39px; }
  .label--front .product-name { top: 206px; font-size: 30px; }
  .tagline {
    position: absolute; left: 0; right: 0; top: 260px;
    font-size: 21px; line-height: 29px; color: var(--brown);
  }
  .front-footer {
    position: absolute; top: 352px; left: 0; right: 0;
    font-family: "Alegreya SC", Georgia, serif; font-weight: 700;
    font-size: 14px; color: var(--brown);
  }
  .front-footer .natural { position: absolute; left: 138px; }
  .front-footer .weight { position: absolute; left: 280px; }
  .natural-dot { position: absolute; left: 186px; top: -20px; width: 18px; height: 12px; border-radius: 9px 9px 2px 2px; background: var(--accent-green); }
  /* back */
  .label--back .brand-mark { top: 20px; width: 42px; height: 42px; }
  .label--back .brand-name { top: 78px; font-size: 30px; }
  .label--back .dotted-rule { top: 123px; left: 80px; right: 80px; }
  .label--back .product-name { top: 131px; font-size: 21px; }
  .ingredients {
    position: absolute; left: 30px; right: 30px;
    font-size: 13.5px; line-height: 17px; text-align: left; color: var(--ink);
  }
  .ingredients--en { top: 164px; }
  .ingredients--alt { top: 222px; font-style: italic; }
  .about {
    position: absolute; left: 30px; top: 296px; width: 160px;
    text-align: justify; font-size: 12.5px; line-height: 15px;
  }
  .about-title { font-family: "Alegreya SC", Georgia, serif; font-weight: 700; font-size: 13px; text-align: left; }
  .result { position: absolute; top: 280px; width: 74px; text-align: center; }
  .result--before { left: 194px; }
  .result--after { left: 260px; }
  .result-photo {
    display: block; margin: 0 auto;
    width: 54px; height: 54px; border-radius: 50%;
    background: var(--face-tone);
    border: 1.5px solid var(--brown);
  }
  .result-caption { font-size: 7.5px; font-weight: 500; color: var(--brown); margin-top: 2px; }
  .back-weight {
    position: absolute; left: 278px; top: 352px;
    font-family: "Alegreya SC", Georgia, serif; font-weight: 700; font-size: 14px; color: var(--brown);
  }
</style>
</head>
<body>

<section class="label label--front">
  <div class="leaf-field" role="img" aria-label="Background of overlapping green leaves"></div>
  <div class="panel">
    <div class="panel-frame"></div>
    <div class="content">
      <span class="brand-mark"></span>
      <h1 class="brand-name"><span class="dot"></span>KIRO SOAP<span class="dot"></span></h1>
      <div class="dotted-rule"></div>
      <h2 class="product-name">JUNGLE OIL</h2>
      <p class="tagline">Ideal formula for all skin types<br>Acne - Skin Irritation - Skin Sensitive</p>
      <div class="front-footer">
        <span class="natural-dot"></span>
        <span class="natural">100% NATURAL</span>
        <span class="weight">100 GM</span>
      </div>
    </div>
  </div>
</section>

<section class="label label--back">
  <div class="leaf-field" role="img" aria-label="Background of overlapping green leaves"></div>
  <div class="panel">
    <div class="panel-frame"></div>
    <div class="content">
      <span class="brand-mark"></span>
      <h1 class="brand-name"><span class="dot"></span>KIRO SOAP<span class="dot"></span></h1>
      <div class="dotted-rule"></div>
      <h2 class="product-name">JUNGLE OIL</h2>
      <p class="ingredients ingredients--en">Ingredienti: Lorem ipsum dolor sit amet, consectetur adipisci elit, sed eiusmod tempor incidunt ut labore et dolore magna aliqua.</p>
      <p class="ingredients ingredients--alt">Ingredienti: Lorem ipsum dolor sit amet, consectetur adipisci elit, sed eiusmod tempor incidunt ut labore et dolore magna aliqua.</p>
      <div class="about">
        <div class="about-title">KIRO SOAP</div>
        Lorem ipsum dolor sit amet, consectetur adipisci elit, sed eiusmod tempor incidunt ut labore et dolore magna aliqua.
      </div>
      <figure class="result result--before">
        <span class="result-photo" role="img" aria-label="Portrait of skin before use"></span>
        <figcaption class="result-caption">Before...</figcaption>
      </figure>
      <figure class="result result--after">
        <span class="result-photo" role="img" aria-label="Portrait of skin after use"></span>
        <figcaption class="result-caption">after use KIRO SOAP</figcaption>
      </figure>
      <span class="back-weight">100 GM</span>
    </div>
  </div>
</section>

</body>
</html>
```